Out Door Living brochure

We need a Great looking brochure to feature the latest in out door living. Showcasing out doors is the new living space.

I'm enclosing our logo and a brochure we had done recently it didn't have enough impact. This one was a single fold you can also provide a tri fold if you see fit. We like the verbiage, but if you can spice it up we would love to see that. This brochure will be added to our sales packet.
Thank you!!!

Target Market(s)

Home owners

Industry/Entity Type

Construction Company

Logo Text

(See logo) Beautiful Homes Built to Last Introducing Outdoor living 2017

Font styles to use
Serif

Requirements
Must have
• Logo and
• Beautiful Homes Built to Last
• Introducing Outdoor living 2017
Nice to have
• Benefits of outdoor living
Should not have
• Bad photos if these don't work let me know we can get others to replace the sapce

```html
<!DOCTYPE html>
<html lang="en">
<head>
<meta charset="utf-8">
<title>Outdoor Living 2017 Brochure</title>
<link href="https://fonts.googleapis.com/css2?family=Crimson+Text:ital,wght@0,400;0,600;0,700;1,400&family=Roboto+Condensed:wght@300;400;700&display=swap" rel="stylesheet">
<style>
  :root{
    --page-bg:#e6e6e6;
    --paper:#ffffff;
    --charcoal:#4a4a4a;
    --ink:#1c1c1c;
    --brand-blue:#3f8fcf;
    --brand-blue-light:#5ba7de;
    --muted:#5a5a5a;
    --photo-sky:#9fc3d8;
    --photo-deck:#5b6670;
  }
  *{margin:0;padding:0;box-sizing:border-box}
  html,body{width:1200px;height:1200px;overflow:hidden;background:var(--page-bg)}
  .canvas{position:relative;width:1200px;height:1200px;background:var(--page-bg)}
  .spread{position:absolute;left:80px;top:200px;width:1040px;height:800px;box-shadow:0 12px 40px rgba(0,0,0,.18)}
  .spread-art{position:absolute;inset:0}
  .panel-text{position:absolute}

  .tagline{left:28px;top:52px;width:330px;font-family:"Crimson Text",serif;font-size:19px;line-height:1.15;color:var(--brand-blue)}
  .photo-caption{left:28px;top:482px;width:440px;font-family:"Crimson Text",serif;font-size:20px;line-height:1.15;letter-spacing:.5px;color:#fff;text-transform:uppercase}
  .contact{left:40px;top:600px;font-family:"Crimson Text",serif;color:var(--ink)}
  .contact h2{font-size:32px;font-weight:700;margin-bottom:8px}
  .contact h2 span{color:var(--brand-blue)}
  .contact p{font-size:17px;line-height:1.25;padding-left:20px}

  .brand{left:700px;top:110px;width:260px;text-align:center;font-family:"Roboto Condensed",sans-serif;font-weight:400;font-size:22px;letter-spacing:2px;color:var(--muted);display:flex;flex-direction:column;align-items:center;gap:14px}
  .brand-mark{width:70px;height:70px;background:var(--brand-blue)}
  .headline{left:580px;top:282px;font-family:"Roboto Condensed",sans-serif;font-size:56px;line-height:58px;text-transform:uppercase}
  .headline .line-dark{color:var(--ink);font-weight:400}
  .headline .line-light{color:#fff;font-weight:700}
  .headline .line-thin{color:var(--ink);font-weight:300}
  .edition{left:660px;top:560px;display:flex;align-items:center;font-family:"Roboto Condensed",sans-serif;font-weight:700}
  .edition-title{font-size:44px;line-height:42px;color:var(--ink);text-transform:uppercase;padding-right:12px;border-right:2px solid var(--ink)}
  .edition-year{font-size:92px;line-height:84px;color:var(--brand-blue);padding-left:12px}
</style>
</head>
<body>
<div class="canvas">
  <div class="spread">
    <svg class="spread-art" width="1040" height="800" viewBox="0 0 1040 800">
      <defs>
        <clipPath id="back-circle"><circle cx="70" cy="400" r="440"/></clipPath>
        <clipPath id="front-circle"><circle cx="970" cy="400" r="440"/></clipPath>
        <linearGradient id="patio-tones" x1="0" y1="0" x2="0" y2="1">
          <stop offset="0" stop-color="var(--photo-sky)"/>
          <stop offset=".35" stop-color="#8aa9a6"/>
          <stop offset=".6" stop-color="#4f8fa3"/>
          <stop offset="1" stop-color="var(--photo-deck)"/>
        </linearGradient>
      </defs>
      <rect class="fold-background" x="0" y="0" width="1040" height="800" fill="var(--charcoal)"/>
      <line x1="520" y1="0" x2="520" y2="800" stroke="#3c3c3c" stroke-width="2"/>

      <g class="back-cover" clip-path="url(#back-circle)">
        <rect x="0" y="0" width="520" height="800" fill="var(--paper)"/>
        <rect x="0" y="130" width="520" height="430" fill="url(#patio-tones)" role="img" aria-label="Photo of a backyard deck with blue cushioned bench seating, a glass-walled fire pit and a palm planter overlooking a lake"/>
        <rect x="0" y="125" width="520" height="4" fill="var(--brand-blue-light)"/>
        <rect x="0" y="561" width="520" height="4" fill="var(--brand-blue-light)"/>
        <rect x="0" y="472" width="520" height="72" fill="rgba(30,30,30,.55)"/>
      </g>

      <g class="front-cover" clip-path="url(#front-circle)">
        <rect x="520" y="0" width="520" height="800" fill="var(--paper)"/>
        <rect x="520" y="268" width="520" height="200" fill="var(--brand-blue)"/>
      </g>
    </svg>

    <p class="panel-text tagline">Innovative ideas that help stretch out the seasons, making it comfy and cozy.</p>
    <p class="panel-text photo-caption">Enjoy your staycation in the comfort of your own back yard.</p>
    <div class="panel-text contact">
      <h2>Contact <span>Us</span></h2>
      <p>555-014-2290</p>
      <p>info@harborridgebuilders.com</p>
      <p>www.harborridgebuilders.com</p>
      <p>1420 Bayview Lane, Fairhaven,</p>
      <p>CA 90000</p>
    </div>

    <div class="panel-text brand">
      <span class="brand-mark"></span>
      <span class="brand-name">HARBOR RIDGE BUILDERS</span>
    </div>
    <h1 class="panel-text headline">
      <span class="line-dark">Beautiful Homes</span><br>
      <span class="line-light">Built to Last</span><br>
      <span class="line-thin">Introducing</span>
    </h1>
    <div class="panel-text edition">
      <span class="edition-title">Outdoor<br>Living</span>
      <span class="edition-year">2017</span>
    </div>
  </div>
</div>
</body>
</html>
```